Business Card Design

I need a bussiness card that have some picture of a van and lorry.
Updates

Hello I could ask you to print business cards and message to the home address?

Industry/Entity Type

Business

Contact Information for Business Card

K&W Haulage LTD
truck and vans fridge
drivers recruitment
k.w-haulage@mailbox-example.com
tel nr 07812450396

```html
<!DOCTYPE html>
<html lang="en">
<head>
<meta charset="utf-8">
<title>K&amp;W Haulage LTD – Business Card</title>
<link href="https://fonts.googleapis.com/css2?family=Questrial&family=Roboto:ital,wght@1,700&display=swap" rel="stylesheet">
<style>
  :root {
    --backdrop: #9d9e99;
    --card: #000000;
    --accent-yellow: #ffd500;
    --contact-yellow: #f2c81a;
    --band-red: #9b1d1d;
    --rule-red: #4a0d0d;
    --ink: #000000;
    --white: #ffffff;
  }
  html, body {
    margin: 0;
    padding: 0;
    width: 1200px;
    height: 743px;
    overflow: hidden;
    background: var(--backdrop);
  }
  .card {
    position: absolute;
    left: 28px;
    top: 33px;
    width: 1142px;
    height: 667px;
    background: var(--card);
    font-family: "Questrial", sans-serif;
  }
  .photo {
    position: absolute;
    top: 176px;
    height: 193px;
  }
  .photo--truck {
    left: 0;
    width: 315px;
    background: linear-gradient(160deg, #c9d3dc 0%, #7d8c99 45%, #2f3a44 75%, #55606a 100%);
  }
  .photo--vans {
    left: 315px;
    width: 269px;
    background: linear-gradient(180deg, #8fb6df 0%, #b9cde2 45%, #5b6878 70%, #3a4350 100%);
  }
  .express-band {
    position: absolute;
    left: 0;
    top: 369px;
    width: 344px;
    height: 48px;
  }
  .express-band__label {
    position: absolute;
    left: 38px;
    top: 0;
    line-height: 48px;
    font-family: "Roboto", sans-serif;
    font-weight: 700;
    font-style: italic;
    font-size: 28px;
    color: var(--white);
  }
  .title-panel {
    position: absolute;
    left: 0;
    top: 0;
    width: 1142px;
    height: 667px;
  }
  .title-panel__text {
    position: absolute;
    left: 618px;
    top: 256px;
    margin: 0;
    font-weight: 400;
    font-size: 31px;
    line-height: 35px;
    color: var(--ink);
  }
  .contact {
    position: absolute;
    left: 0;
    width: 1142px;
    top: 494px;
    display: flex;
    justify-content: center;
    align-items: center;
    gap: 14px;
    font-size: 31px;
    color: var(--contact-yellow);
  }
  .contact__item {
    display: flex;
    align-items: center;
    gap: 10px;
  }
  .contact__icon {
    width: 30px;
    height: 30px;
  }
  .divider {
    position: absolute;
    left: 0;
    top: 597px;
    width: 1142px;
    height: 2px;
    background: var(--rule-red);
  }
</style>
</head>
<body>
  <div class="card">
    <div class="photo photo--truck" role="img" aria-label="Photo of a refrigerated lorry driving on a mountain road"></div>
    <div class="photo photo--vans" role="img" aria-label="Photo of two delivery vans driving on a city road"></div>

    <div class="express-band">
      <svg width="344" height="48" viewBox="0 0 344 48" aria-hidden="true">
        <polygon points="0,0 344,0 312,48 0,48" fill="var(--band-red)"/>
      </svg>
      <span class="express-band__label">Express Delivery</span>
    </div>

    <svg class="title-panel" viewBox="0 0 1142 667" aria-hidden="true">
      <polygon points="598,245 1140,245 1140,177 1097,177 982,245" fill="var(--accent-yellow)"/>
      <rect x="598" y="245" width="542" height="126" fill="var(--accent-yellow)"/>
    </svg>
    <h1 class="title-panel__text">K&amp;W Haulage LTD truck<br>and<br>vans fridge drivers recruitment</h1>

    <div class="contact">
      <span class="contact__item">
        <svg class="contact__icon" viewBox="0 0 30 30" aria-hidden="true">
          <circle cx="15" cy="15" r="13" fill="none" stroke="var(--contact-yellow)" stroke-width="2"/>
          <text x="15" y="21" text-anchor="middle" font-size="17" font-family="Questrial, sans-serif" fill="var(--contact-yellow)">@</text>
        </svg>
        k.w-haulage@mailbox-example.com
      </span>
      <span class="contact__item">
        <svg class="contact__icon" viewBox="0 0 30 30" aria-hidden="true">
          <circle cx="15" cy="15" r="13" fill="none" stroke="var(--contact-yellow)" stroke-width="2"/>
          <path d="M10 8.5 L12.8 8 L14.2 11.6 L12.5 13 C13.3 14.9 15 16.7 17 17.6 L18.4 15.9 L22 17.3 L21.5 20 C21.2 21 20.2 21.6 19.2 21.4 C13.6 20.4 9.6 16.4 8.6 10.8 C8.4 9.8 9 8.8 10 8.5 Z" fill="var(--contact-yellow)"/>
        </svg>
        07812450396
      </span>
    </div>

    <div class="divider"></div>
  </div>
</body>
</html>
```